KLV Messaging - veteran and exclusive boutique copywriting agency

PROJECT NEEDS:
1. Website design - full homepage design and inner page top banner design
2. Logo design
* Please see attached Briefs (Word Docs) for descriptions of what is needed for 1 and 2 above.
ABOUT THE CLIENT:
KLV Messaging is a veteran and exclusive boutique copywriting agency run by Marcus Holloway. Marcus is an award-winning published novelist and an accomplished executive ghostwriter with articles regularly published prominent technology publications like Brisk, ByteHarbor, FoundryPulse, and more. For nearly three decades, Marcus has focused solely on the technology sector - serving clients in Israel, Europe and the US.

Target Market(s)

hi-tech companies run by serious, confident professionals.

Industry/Entity Type

Business

Number of Pages Required

2 page

Font styles to use
Sans Serif
Other font styles liked:
• font should be modern

Colors
0054AA
0677BA
7BADD7
CADEEF
E8F1F8
F0912C
F2A743
F7CA91
FBE8D2
FDF5EE

Requirements
Must have
• psd files for logo, homepage design, and inner page top banner design
Nice to have
• Please see attached Website and Logo Design Briefs (Word Docs)
Should not have

```html
<!DOCTYPE html>
<html lang="en">
<head>
<meta charset="utf-8">
<title>KLV Messaging</title>
<link href="https://fonts.googleapis.com/css2?family=Poppins:wght@400;500;600;700;800&display=swap" rel="stylesheet">
<style>
:root{
  --blue-deep:#0054aa;
  --blue:#0677ba;
  --blue-band:#1581c7;
  --blue-soft:#7badd7;
  --blue-pale:#ddeffa;
  --orange:#f0912c;
  --orange-dark:#e07f1a;
  --orange-soft:#f7ca91;
  --grey-band:#e5e5e5;
  --grey-test:#ebe9ea;
  --grey-shade:#dcdbdb;
  --ink:#2a2a2a;
  --white:#ffffff;
}
*{margin:0;padding:0;box-sizing:border-box}
html,body{width:1200px;height:3515px;overflow:hidden}
body{font-family:'Poppins',sans-serif;color:var(--white);position:relative;background:var(--white)}
section,header,footer{position:absolute;left:0;width:1200px;overflow:hidden}
.abs{position:absolute}
.bg{position:absolute;left:0;top:0}
.brand{font-weight:700;font-size:34px;color:var(--white);letter-spacing:.5px;white-space:nowrap}
.nav a{position:absolute;font-size:13px;font-weight:500;color:var(--white);text-decoration:none;text-transform:uppercase;white-space:nowrap}
.btn{position:absolute;background:var(--orange);color:var(--white);font-weight:500;display:flex;align-items:center;justify-content:center;border-radius:3px}
.ghost{position:absolute;font-weight:800;white-space:nowrap;line-height:1}
.h2{position:absolute;font-weight:700;font-size:55px;line-height:1;white-space:nowrap}
.photo{position:absolute}

/* hero */
.hero{top:0;height:651px;background:var(--blue)}
.hero h1{position:absolute;left:85px;top:222px;font-size:55px;font-weight:700;line-height:1.1}
.hero p{position:absolute;left:85px;top:298px;font-size:24px;font-weight:500;line-height:1.15;width:560px}

/* clients */
.clients{top:651px;height:171px;background:var(--grey-band)}
.client{position:absolute;top:68px;width:170px;text-align:center;font-size:26px;font-weight:600;color:#3a3f4a;white-space:nowrap}
.arrow{position:absolute;top:80px;width:22px;height:22px;background:#c4c4c4;border-radius:2px}

/* services */
.services{top:822px;height:624px;background:var(--orange)}
.services .intro{position:absolute;left:75px;top:180px;width:420px;font-size:18.5px;line-height:1.22}
.list{position:absolute;left:78px;top:323px;list-style:none}
.list li{display:flex;align-items:center;height:27px;font-size:20px;font-weight:500}
.list svg{margin-right:14px}

/* why */
.why{top:1446px;height:660px;background:var(--blue-band)}
.card{position:absolute;top:256px;width:335px;height:305px;background:var(--blue-pale);border-radius:6px;padding:20px 20px}
.card h3{font-size:29px;font-weight:600;color:var(--blue);line-height:1.2}
.card .rule{width:93px;height:3px;background:var(--orange);margin:12px 0 18px}
.card h4{font-size:17.5px;font-weight:600;color:var(--blue-deep);margin-left:2px;white-space:nowrap}
.card p{font-size:14px;color:#27384a;line-height:1.2;margin:8px 0 0 2px;width:270px}
.card .btn{position:relative;width:119px;height:35px;font-size:14px;margin:17px 0 0 2px}

/* testimonials */
.testimonials{top:2106px;height:740px;background:var(--grey-test)}
.quote{position:absolute;width:380px;color:var(--ink)}
.quote .avatar{position:absolute;left:-125px;top:44px;width:104px;height:104px;border-radius:50%;border:4px solid var(--white);background:radial-gradient(circle at 50% 40%,#c9c2ba,#5c6470)}
.quote .mark{position:absolute;left:-15px;top:-4px;font-size:28px;color:#777;font-weight:700;line-height:1}
.quote .endmark{position:absolute;right:105px;top:102px;font-size:28px;color:#777;font-weight:700;line-height:1}
.quote p{position:absolute;left:0;top:22px;width:265px;font-size:12.5px;line-height:1.42;color:#555}
.quote .name{position:absolute;left:0;top:132px;font-size:13px;font-weight:600;color:#111}
.quote .role{position:absolute;left:0;top:150px;font-size:8.5px;color:#555}
.quote .stars{position:absolute;left:0;top:163px;font-size:11px;color:var(--orange);letter-spacing:1px}

/* newsletter */
.newsletter{top:2846px;height:314px;background:var(--orange)}
.newsletter label{position:absolute;left:143px;top:208px;font-size:28px;font-weight:500}
.newsletter .field{position:absolute;left:423px;top:202px;width:452px;height:53px;background:#efefef;border-radius:3px;color:#9a9a9a;font-size:16px;padding:0 16px;display:flex;align-items:center}
.newsletter .submit{position:absolute;left:882px;top:202px;width:190px;height:53px;background:var(--blue-band);border-radius:3px;font-size:18px;font-weight:500;display:flex;align-items:center;justify-content:center}

/* footer */
.site-footer{top:3160px;height:355px;background:var(--blue-band)}
.social{position:absolute;top:230px;width:50px;height:50px;border:2px solid var(--white);border-radius:50%}
.site-footer .line{position:absolute;left:149px;top:310px;width:902px;height:1px;background:rgba(255,255,255,.7)}
.site-footer .copy{position:absolute;left:0;width:1200px;top:324px;text-align:center;font-size:10.5px}
</style>
</head>
<body>

<header class="hero">
  <svg class="bg" width="1200" height="651" viewBox="0 0 1200 651"><polygon points="427,651 1200,293 1200,651" fill="#f0912c"/></svg>
  <div class="abs brand" style="left:85px;top:42px">KLV Messaging</div>
  <nav class="nav">
    <a style="left:523px;top:57px">About</a><a style="left:610px;top:57px">Services</a><a style="left:714px;top:57px">Industries</a><a style="left:833px;top:57px">Portfolio</a><a style="left:946px;top:57px">Clients</a><a style="left:1042px;top:57px">Contact</a>
  </nav>
  <h1>Your voice, My words</h1>
  <p>Copywriting and executive ghostwriting that speaks for your vision and your technology.</p>
  <div class="btn" style="left:85px;top:378px;width:178px;height:44px;font-size:19px">Contact Me</div>
  <div class="photo" role="img" aria-label="Portrait of Marcus Holloway in a light blue shirt" style="left:737px;top:130px;width:280px;height:521px;border-radius:110px 110px 0 0;background:linear-gradient(180deg,#c9a48e 0%,#a9cbe8 28%,#8fb6dc 65%,#4e6f95 100%)"></div>
</header>

<section class="clients">
  <div class="arrow" style="left:74px"></div>
  <div class="client" style="left:135px">Corvix</div>
  <div class="client" style="left:335px">Halden Bio</div>
  <div class="client" style="left:533px">Tessera</div>
  <div class="client" style="left:704px">Brightforge</div>
  <div class="client" style="left:886px">Pyxel</div>
  <div class="arrow" style="left:1102px"></div>
</section>

<section class="services">
  <svg class="bg" width="1200" height="624" viewBox="0 0 1200 624"><polygon points="0,352 723,624 0,624" fill="#e07f1a"/></svg>
  <div class="ghost" style="left:73px;top:50px;font-size:90px;color:rgba(255,255,255,.25)">SERVICES</div>
  <div class="h2" style="left:75px;top:102px">What I Do</div>
  <p class="intro">Since 2001, KLV Messaging has had the opportunity to create collateral and content for tens of companies across a wide range of industries. Following is a small selection of recent projects:</p>
  <ul class="list">
    <li><svg width="18" height="18" viewBox="0 0 18 18"><rect x="1" y="3" width="14" height="14" fill="none" stroke="#fff" stroke-width="1.6"/><path d="M4 9l4 4 8-11" fill="none" stroke="#fff" stroke-width="2"/></svg>Contributed Content</li>
    <li><svg width="18" height="18" viewBox="0 0 18 18"><rect x="1" y="3" width="14" height="14" fill="none" stroke="#fff" stroke-width="1.6"/><path d="M4 9l4 4 8-11" fill="none" stroke="#fff" stroke-width="2"/></svg>Blog Content</li>
    <li><svg width="18" height="18" viewBox="0 0 18 18"><rect x="1" y="3" width="14" height="14" fill="none" stroke="#fff" stroke-width="1.6"/><path d="M4 9l4 4 8-11" fill="none" stroke="#fff" stroke-width="2"/></svg>White Papers &amp; E-Books</li>
    <li><svg width="18" height="18" viewBox="0 0 18 18"><rect x="1" y="3" width="14" height="14" fill="none" stroke="#fff" stroke-width="1.6"/><path d="M4 9l4 4 8-11" fill="none" stroke="#fff" stroke-width="2"/></svg>Case Studies</li>
    <li><svg width="18" height="18" viewBox="0 0 18 18"><rect x="1" y="3" width="14" height="14" fill="none" stroke="#fff" stroke-width="1.6"/><path d="M4 9l4 4 8-11" fill="none" stroke="#fff" stroke-width="2"/></svg>Web Site Content</li>
    <li><svg width="18" height="18" viewBox="0 0 18 18"><rect x="1" y="3" width="14" height="14" fill="none" stroke="#fff" stroke-width="1.6"/><path d="M4 9l4 4 8-11" fill="none" stroke="#fff" stroke-width="2"/></svg>Video - Concept and Script</li>
    <li><svg width="18" height="18" viewBox="0 0 18 18"><rect x="1" y="3" width="14" height="14" fill="none" stroke="#fff" stroke-width="1.6"/><path d="M4 9l4 4 8-11" fill="none" stroke="#fff" stroke-width="2"/></svg>Press Releases</li>
    <li><svg width="18" height="18" viewBox="0 0 18 18"><rect x="1" y="3" width="14" height="14" fill="none" stroke="#fff" stroke-width="1.6"/><path d="M4 9l4 4 8-11" fill="none" stroke="#fff" stroke-width="2"/></svg>Collateral (brochures, datasheets and more)</li>
  </ul>
  <div class="abs" style="left:655px;top:175px;font-size:62px;font-weight:700;color:rgba(251,232,210,.6);white-space:nowrap">KLV Messaging</div>
</section>

<section class="why">
  <svg class="bg" width="1200" height="660" viewBox="0 0 1200 660"><polygon points="491,660 1200,315 1200,660" fill="#f0912c"/></svg>
  <div class="ghost" style="left:68px;top:80px;font-size:104px;color:rgba(123,173,215,.4)">CHOOSE</div>
  <div class="h2" style="left:72px;top:146px">Why Choose Me</div>
  <div class="card" style="left:74px"><h3>Messaging</h3><div class="rule"></div><h4>The Value of a Fresh Perspective</h4><p>Could you be reaching farther? Clearly defined, accurately targeted messaging is crucial.</p><div class="btn">Read More</div></div>
  <div class="card" style="left:431px"><h3>Collateral</h3><div class="rule"></div><h4>Concise, Effective, Creative</h4><p>Could you be reaching farther? Clearly defined, accurately targeted messaging is crucial.</p><div class="btn">Read More</div></div>
  <div class="card" style="left:789px"><h3>Content Marketing</h3><div class="rule"></div><h4>Giving Voice to Your Vision</h4><p>Could you be reaching farther? Clearly defined, accurately targeted messaging is crucial.</p><div class="btn">Read More</div></div>
</section>

<div class="photo" role="img" aria-label="Black and white portrait of Marcus Holloway" style="left:785px;top:1215px;width:348px;height:487px;border-radius:120px 120px 0 0;background:linear-gradient(180deg,#9b9b9b 0%,#d8d8d8 35%,#bdbdbd 70%,#6f6f6f 100%)"></div>

<section class="testimonials">
  <svg class="bg" width="1200" height="740" viewBox="0 0 1200 740"><polygon points="0,412 683,740 0,740" fill="#dcdbdb"/></svg>
  <div class="ghost" style="left:0;width:1200px;text-align:center;top:70px;font-size:88px;color:rgba(255,255,255,.9)">TESTIMONIALS</div>
  <div class="h2" style="left:0;width:1092px;text-align:center;top:112px;color:var(--blue-band)">What they’re saying</div>

  <div class="quote" style="left:273px;top:228px"><div class="avatar" role="img" aria-label="Client portrait"></div><span class="mark">“</span><p>Lorem ipsum, or lipsum as it is sometimes known, is dummy text used in laying out print, graphic or web designs. The passage is attributed to an unknown typesetter in the 15th century</p><span class="endmark">”</span><div class="name">Dana Whitfield</div><div class="role">CEO, Northlane Inc.</div><div class="stars">★★★★★</div></div>
  <div class="quote" style="left:684px;top:228px"><div class="avatar" role="img" aria-label="Client portrait" style="background:radial-gradient(circle at 50% 40%,#e4d6c8,#b9a692)"></div><span class="mark">“</span><p>Lorem ipsum, or lipsum as it is sometimes known, is dummy text used in laying out print, graphic or web designs. The passage is attributed to an unknown typesetter in the 15th century</p><span class="endmark">”</span><div class="name">Dana Whitfield</div><div class="role">CEO, Northlane Inc.</div><div class="stars">★★★★★</div></div>
  <div class="quote" style="left:273px;top:476px"><div class="avatar" role="img" aria-label="Client portrait"></div><span class="mark">“</span><p>Lorem ipsum, or lipsum as it is sometimes known, is dummy text used in laying out print, graphic or web designs. The passage is attributed to an unknown typesetter in the 15th century</p><span class="endmark">”</span><div class="name">Dana Whitfield</div><div class="role">CEO, Northlane Inc.</div><div class="stars">★★★★★</div></div>
  <div class="quote" style="left:686px;top:476px"><div class="avatar" role="img" aria-label="Client portrait"></div><span class="mark">“</span><p>Lorem ipsum, or lipsum as it is sometimes known, is dummy text used in laying out print, graphic or web designs. The passage is attributed to an unknown typesetter in the 15th century</p><span class="endmark">”</span><div class="name">Dana Whitfield</div><div class="role">CEO, Northlane Inc.</div><div class="stars">★★★★★</div></div>
</section>

<section class="newsletter">
  <div class="ghost" style="left:0;width:1200px;text-align:center;top:78px;font-size:80px;color:rgba(247,202,145,.55)">SIGNUP</div>
  <div class="h2" style="left:0;width:1200px;text-align:center;top:104px">Newsletter</div>
  <label>Sign For Newsletter</label>
  <div class="field">Enter your Email</div>
  <div class="submit">SUBSCRIBE</div>
</section>

<footer class="site-footer">
  <div class="abs brand" style="left:0;width:1200px;text-align:center;top:58px">KLV Messaging</div>
  <nav class="nav">
    <a style="left:314px;top:184px">About</a><a style="left:401px;top:184px">Services</a><a style="left:505px;top:184px">Industries</a><a style="left:621px;top:184px">Portfolio</a><a style="left:736px;top:184px">Clients</a><a style="left:830px;top:184px">Contact</a>
  </nav>
  <div class="social" style="left:519px" role="img" aria-label="Social profile link"></div>
  <div class="social" style="left:578px" role="img" aria-label="Social profile link"></div>
  <div class="social" style="left:637px" role="img" aria-label="Social profile link"></div>
  <div class="line"></div>
  <div class="copy">Copyright © 2023 All Rights Reserved By KLV</div>
</footer>

</body>
</html>
```